Information poster for parquet showroom

We are a parquet shop from germany and need some information poster for our showroom, to show our costumers some important information about parqut directly. The three posters are about reasons for parquet, and there are two types of paper on the subject. We would like to place the posters in a wooden frame. The design should be modern but simple. Enclosed I send you some of my ideas but it does not have to be like this. Can be completely different. I also send you some pictures of our showroom. 1st poster: Why parquet (dimension: 90x130 cm) Why parquet? - brings nature into your home - ecologically sustainable raw material - pleasantly warm - timeless% 26amp; high quality optics - durable% 26amp; reparable flooring - improved indoor climate - unique ride 2. Advantages oiled - tangible wood structure - natural appearance - scratches less present - partial repair possible advantage varnished - very easy-care - classic% 26amp; elegant appearance - protection against dirt and moisture - variable gloss level 3. Poster: overview of the hardness of different kinds of wood (dimension: 67x130 cm) wood hardness according to Brinell in N / mm² maple europ. 28 maple canadian. 35 birch 27 beech 33 oak 34 alder 17 ash 37 doussie 42 spruce 12 kambala 30 chestnut 18 pine 20 cherry european. 31 Larch 19 Merbau 44 Robinia 48 Sucupira 57 Elm 30 Wenge 45

```html
<!DOCTYPE html>
<html lang="en">
<head>
<meta charset="utf-8">
<title>Why Parquet?</title>
<link rel="stylesheet" href="https://fonts.googleapis.com/css2?family=Anton&display=swap">
<style>
  :root {
    --paper: #efefef;
    --paper-deep: #e2e2e2;
    --ink-dark: #404040;
    --ink-mid: #707070;
    --ink-light: #aaaaaa;
  }
  html, body {
    margin: 0;
    padding: 0;
    overflow: hidden;
  }
  .poster {
    position: relative;
    width: 831px;
    height: 1200px;
    overflow: hidden;
    background: var(--paper);
    font-family: "Anton", "Impact", sans-serif;
  }
  .backdrop {
    position: absolute;
    inset: 0;
    background: linear-gradient(160deg, #f3f3f3 0%, var(--paper-deep) 45%, #f1f1f1 70%, var(--paper-deep) 100%);
  }
  .frame {
    position: absolute;
    left: 15px;
    top: 17px;
    width: 798px;
    height: 1165px;
    border: 2px solid var(--ink-dark);
  }
  .headline {
    position: absolute;
    left: 0;
    top: 0;
    width: 831px;
    height: 500px;
  }
  .headline text {
    font-family: "Anton", "Impact", sans-serif;
  }
  .headline-why { fill: var(--ink-dark); }
  .headline-parquet { fill: var(--ink-mid); }
  .question-shadow { fill: var(--ink-dark); }
  .question-face { fill: var(--ink-light); }
  .reasons {
    position: absolute;
    left: 0;
    top: 0;
    margin: 0;
    padding: 0;
    list-style: none;
  }
  .reason {
    position: absolute;
    left: 69px;
    height: 40px;
    display: flex;
    align-items: center;
    white-space: nowrap;
    font-size: 40px;
    line-height: 1;
    color: var(--ink-dark);
  }
  .reason-marker {
    position: relative;
    width: 20px;
    height: 20px;
    margin-right: 28px;
    flex: none;
  }
  .reason-marker::before,
  .reason-marker::after {
    content: "";
    position: absolute;
    width: 17px;
    height: 17px;
  }
  .reason-marker::before {
    left: 5px;
    top: 5px;
    background: var(--ink-dark);
  }
  .reason-marker::after {
    left: 0;
    top: 0;
    background: var(--ink-light);
  }
</style>
</head>
<body>
<main class="poster">
  <div class="backdrop" role="img" aria-label="Soft grey background with a faint pattern of overlapping hexagons"></div>
  <div class="frame"></div>

  <svg class="headline" viewBox="0 0 831 500" aria-label="Why parquet?">
    <g transform="rotate(2 323 165)">
      <text class="headline-why" x="143" y="243" font-size="220" textLength="360" lengthAdjust="spacingAndGlyphs">WHY</text>
    </g>
    <g transform="translate(125 419) rotate(-7)">
      <text class="headline-parquet" x="0" y="0" font-size="118" textLength="392" lengthAdjust="spacingAndGlyphs">PARQUET</text>
    </g>
    <g transform="translate(556 428) rotate(-8)">
      <text class="question-shadow" x="13" y="10" font-size="312" textLength="145" lengthAdjust="spacingAndGlyphs">?</text>
      <text class="question-face" x="0" y="0" font-size="312" textLength="145" lengthAdjust="spacingAndGlyphs">?</text>
    </g>
  </svg>

  <ul class="reasons">
    <li class="reason" style="top:567px"><span class="reason-marker"></span>BRINGS NATURE INTO YOUR HOME</li>
    <li class="reason" style="top:651px"><span class="reason-marker"></span>ECOLOGICALLY SUSTAINABLE RAW MATERIAL</li>
    <li class="reason" style="top:735px"><span class="reason-marker"></span>PLEASANTLY WARM</li>
    <li class="reason" style="top:819px"><span class="reason-marker"></span>TIMELESS% 26AMP; HIGH QUALITY OPTICS</li>
    <li class="reason" style="top:904px"><span class="reason-marker"></span>DURABLE% 26AMP; REPARABLE FLOORING</li>
    <li class="reason" style="top:993px"><span class="reason-marker"></span>IMPROVED INDOOR CLIMATE</li>
    <li class="reason" style="top:1077px"><span class="reason-marker"></span>UNIQUE RIDE</li>
  </ul>
</main>
</body>
</html>
```